Pricing sheet For Acupuncture Clinic - Remake Attached Work

Right Now I have 4 pricing sheets that look very disorganized. They are for 4 different options of services I offer with 3 different options to pay for each service (pay each time you come in, prepaid package, or a monthly option). People get confused from this outline so looking to make this easier to understand and better looking. You can reorganize the pricing as you see fit as long as it makes sense. (ex: using columns or rows or a graph) These images are going to be made into standard sized posters (i think that is 5 feet by 7 feet?)

Instead of designing all 4 of the attached files below you can choose 1 of them to show your example of work. I will assume that style will apply to all 4 sheets if I choose your work - also need 1 sheet that can print out on paper that will show all treatments on front and back of paper.

Thank you
Mark

Target Market(s)

Spa Industry

Industry/Entity Type

Clinic

Font styles to use
Serif
Sans Serif
Decorative
Script

Colors
33a6d7
ffffff
000000

Requirements
Nice to have
• clean - organized -
Should not have
• pictures of acupuncture needles. anything sharp. anything that might make people feel afraid of getting the treatments or look painful

```html
<!DOCTYPE html>
<html lang="en">
<head>
<meta charset="utf-8">
<title>Cosmetic Acupuncture Pricing</title>
<link rel="stylesheet" href="https://fonts.googleapis.com/css2?family=Great+Vibes&family=Pinyon+Script&family=Quicksand:wght@300;400&family=Open+Sans:wght@400&display=swap">
<style>
  :root {
    --brand-blue: #33a6d7;
    --white: #ffffff;
    --ink: #000000;
    --canvas: #ffffff;
    --frame: #3a3a3a;
  }
  * { margin: 0; padding: 0; box-sizing: border-box; }
  html, body {
    width: 1200px; height: 1200px; overflow: hidden;
    background: var(--canvas);
  }
  .poster {
    position: absolute;
    left: 202px; top: 44px;
    width: 796px; height: 1112px;
    background: var(--white);
    border: 1px solid var(--frame);
    overflow: hidden;
  }
  .header-band {
    position: absolute; left: 0; top: 0;
    width: 100%; height: 190px;
    background: var(--brand-blue);
    box-shadow: 0 3px 5px rgba(0,0,0,0.35);
    text-align: center;
    color: var(--white);
  }
  .title {
    position: absolute; left: 0; right: 0; top: 10px;
    font-family: "Pinyon Script", cursive;
    font-size: 86px; line-height: 1;
    text-shadow: 3px 4px 5px rgba(0,0,0,0.45);
    letter-spacing: 1px;
  }
  .subtitle {
    position: absolute; left: 0; right: 0; top: 120px;
    font-family: "Quicksand", sans-serif; font-weight: 300;
    font-size: 40px; line-height: 1.2;
    text-shadow: 2px 3px 4px rgba(0,0,0,0.4);
  }
  .section-heading {
    position: absolute; left: 0; right: 0;
    text-align: center;
    font-family: "Great Vibes", cursive;
    font-size: 60px; line-height: 1;
    color: var(--ink);
    font-weight: 700;
    -webkit-text-stroke: 0.6px var(--ink);
  }
  .section-heading sup {
    font-family: "Open Sans", sans-serif;
    font-size: 18px; vertical-align: 28px;
    -webkit-text-stroke: 0;
    font-weight: 400;
  }
  .price-line {
    position: absolute; left: 0; right: 0;
    text-align: center;
    font-family: "Quicksand", sans-serif; font-weight: 300;
    font-size: 46px; line-height: 1;
    color: var(--brand-blue);
    white-space: nowrap;
  }
  .price-row {
    position: absolute; left: 115px;
    display: flex;
    font-family: "Quicksand", sans-serif; font-weight: 300;
    font-size: 46px; line-height: 1;
    color: var(--brand-blue);
    white-space: nowrap;
  }
  .price-row .qty { width: 360px; }
  .price-row .dash { width: 120px; text-align: center; }
  .footer-band {
    position: absolute; left: 0; bottom: 0;
    width: 100%; height: 138px;
    background: var(--brand-blue);
    color: var(--white);
    font-family: "Open Sans", sans-serif;
    font-size: 12.5px; line-height: 18px;
    padding: 38px 0 0 98px;
  }
  .footer-band .indent { padding-left: 8px; }
</style>
</head>
<body>
  <main class="poster">
    <header class="header-band">
      <h1 class="title">Cosmetic Acupuncture</h1>
      <p class="subtitle">Includes Body Acupuncture</p>
    </header>

    <h2 class="section-heading" style="top: 222px;">Single Treatment</h2>
    <p class="price-line" style="top: 290px;">$130 per treatment</p>

    <h2 class="section-heading" style="top: 402px;">1 year Pre - Paid Package<sup>#</sup></h2>
    <div class="price-row" style="top: 478px;"><span class="qty">12&nbsp; Treatments</span><span class="dash">-</span><span class="amount">$900</span></div>
    <div class="price-row" style="top: 540px;"><span class="qty">24 Treatments</span><span class="dash">-</span><span class="amount">$1400</span></div>

    <h2 class="section-heading" style="top: 670px;">Monthly Autopay Packages<sup>*</sup></h2>
    <p class="price-line" style="top: 746px;">4 Treatments per month - $280</p>
    <p class="price-line" style="top: 807px;">8 Treatments per month - $480</p>
    <p class="price-line" style="top: 868px;">12 Treatments per month - $600</p>

    <footer class="footer-band">
      <p>*Monthly unused treatments can be rolled-over. Monthly Autopay can be cancelled after 4 months.</p>
      <p class="indent">Unused treatments are forfeited 3 months after cancellation.</p>
      <p># pre - paid package expires after 1 year, unused treatments are fortfeited.</p>
    </footer>
  </main>
</body>
</html>
```